Velmor new etikitka

Velmori food company founded a new company therefore indz should be attractive for customers to put a picture which I took to the waters of the picture beautifully depicts the mountain which I would love to use my juice on the label of being the cherry juice range, apricots, apples, assortment, etc.

Industry/Entity Type

It Company

Font styles to use
Decorative
Script

```html
<!DOCTYPE html>
<html lang="en">
<head>
<meta charset="utf-8">
<title>Velmor juice labels</title>
<link rel="stylesheet" href="https://fonts.googleapis.com/css2?family=Fredoka:wght@500;600&family=Open+Sans:wght@400;600&display=swap">
<style>
  :root {
    --page: #ffffff;
    --paper: #ffffff;
    --peach: #f4871c;
    --peach-strip: #f7931e;
    --apple: #9cc42a;
    --apple-strip: #a9cf35;
    --cherry-brand: #5b1a20;
    --cherry-strip: #5e1c24;
    --ink-light: rgba(255,255,255,0.92);
    --mountain: #9aa3ab;
    --mountain-dark: #4f5962;
    --mist: #eef1f3;
  }
  * { box-sizing: border-box; margin: 0; padding: 0; }
  html, body { width: 1200px; height: 900px; overflow: hidden; background: var(--page); }
  .canvas { position: relative; width: 1200px; height: 900px; }

  .label {
    position: absolute; top: 300px; width: 340px; height: 300px;
    display: flex; background: var(--paper);
    box-shadow: 0 0 0 1px #ececec;
  }
  .label--peach  { left: 50px; }
  .label--apple  { left: 430px; }
  .label--cherry { left: 810px; }

  .label__front { position: relative; width: 250px; height: 100%; }
  .label__brand {
    position: absolute; left: 12px; top: 26px;
    font-family: "Fredoka", sans-serif; font-weight: 600;
    font-size: 54px; line-height: 1; letter-spacing: 0.5px;
  }
  .label__flavour {
    position: absolute; right: 24px; top: 84px;
    font-family: "Fredoka", sans-serif; font-weight: 600;
    font-size: 22px; line-height: 1;
  }
  .label__photo {
    position: absolute; left: 0; top: 118px; width: 250px; height: 182px;
  }
  .label__volume {
    position: absolute; right: 8px; bottom: 32px;
    font-family: "Open Sans", sans-serif; font-size: 16px; color: #c8c8c8;
  }

  .label__strip {
    width: 90px; height: 100%; padding: 26px 8px 0;
    font-family: "Open Sans", sans-serif; color: var(--ink-light);
  }
  .strip__title { font-size: 9px; font-weight: 600; margin-bottom: 6px; }
  .strip__text { font-size: 6.5px; line-height: 1.45; margin-bottom: 12px; }
  .strip__heading { font-size: 8px; font-weight: 600; margin-bottom: 4px; }
  .strip__note { font-size: 9px; margin-top: 4px; opacity: 0.85; }

  .label--peach .label__brand, .label--peach .label__flavour { color: var(--peach); }
  .label--peach .label__strip { background: var(--peach-strip); }
  .label--apple .label__brand, .label--apple .label__flavour { color: var(--apple); }
  .label--apple .label__strip { background: var(--apple-strip); }
  .label--cherry .label__brand, .label--cherry .label__flavour { color: var(--cherry-brand); }
  .label--cherry .label__strip { background: var(--cherry-strip); }
</style>
</head>
<body>
<main class="canvas">

  <section class="label label--peach">
    <div class="label__front">
      <div class="label__brand">Velmor</div>
      <div class="label__flavour">peach</div>
      <svg class="label__photo" viewBox="0 0 250 182" role="img" aria-label="Photo of snowy mountain peaks with two ripe peaches and leaves in front">
        <defs>
          <linearGradient id="peach-scene" x1="0" y1="0" x2="1" y2="1">
            <stop offset="0" stop-color="#f2f4f5"/>
            <stop offset="0.4" stop-color="#8e979f"/>
            <stop offset="0.75" stop-color="#f0a253"/>
            <stop offset="1" stop-color="#f7f2ec"/>
          </linearGradient>
        </defs>
        <rect width="250" height="182" fill="url(#peach-scene)"/>
      </svg>
    </div>
    <div class="label__strip">
      <p class="strip__title">Velmor peach</p>
      <p class="strip__text">Pure juice pressed from ripe mountain fruit.</p>
      <p class="strip__heading">Ingredients</p>
      <p class="strip__text">Peach, water, cane sugar.</p>
      <p class="strip__text">Made by Velmori Ltd.</p>
      <p class="strip__note">No preservatives</p>
    </div>
  </section>

  <section class="label label--apple">
    <div class="label__front">
      <div class="label__brand">Velmor</div>
      <div class="label__flavour">apple</div>
      <svg class="label__photo" viewBox="0 0 250 182" role="img" aria-label="Photo of snowy mountain peaks with a green apple and a cut apple half">
        <defs>
          <linearGradient id="apple-scene" x1="0" y1="0" x2="1" y2="1">
            <stop offset="0" stop-color="#f2f4f5"/>
            <stop offset="0.4" stop-color="#8e979f"/>
            <stop offset="0.72" stop-color="#8dbf3a"/>
            <stop offset="1" stop-color="#f4f6ef"/>
          </linearGradient>
        </defs>
        <rect width="250" height="182" fill="url(#apple-scene)"/>
      </svg>
      <div class="label__volume">200 ml</div>
    </div>
    <div class="label__strip">
      <p class="strip__title">Velmor apple</p>
      <p class="strip__text">Pure juice pressed from ripe mountain fruit.</p>
      <p class="strip__heading">Ingredients</p>
      <p class="strip__text">Apple, water, cane sugar.</p>
      <p class="strip__text">Made by Velmori Ltd.</p>
      <p class="strip__note">No preservatives</p>
    </div>
  </section>

  <section class="label label--cherry">
    <div class="label__front">
      <div class="label__brand">Velmor</div>
      <div class="label__flavour">cherry</div>
      <svg class="label__photo" viewBox="0 0 250 182" role="img" aria-label="Photo of snowy mountain peaks with a bunch of red cherries on stems">
        <defs>
          <linearGradient id="cherry-scene" x1="0" y1="0" x2="1" y2="1">
            <stop offset="0" stop-color="#f2f4f5"/>
            <stop offset="0.4" stop-color="#8e979f"/>
            <stop offset="0.72" stop-color="#b3202e"/>
            <stop offset="1" stop-color="#f6eeee"/>
          </linearGradient>
        </defs>
        <rect width="250" height="182" fill="url(#cherry-scene)"/>
      </svg>
      <div class="label__volume">200 ml</div>
    </div>
    <div class="label__strip">
      <p class="strip__title">Velmor cherry</p>
      <p class="strip__text">Pure juice pressed from ripe mountain fruit.</p>
      <p class="strip__heading">Ingredients</p>
      <p class="strip__text">Cherry, water, cane sugar.</p>
      <p class="strip__text">Made by Velmori Ltd.</p>
      <p class="strip__note">No preservatives</p>
    </div>
  </section>

</main>
</body>
</html>
```